We have a new logo so we need to change our business card

We're super Happy with our current cards but I think with a new logo should come a new design. I wouldn't mind seeing the icons that we used on the back last time reused on this card. Please feel free to visit our website to get a sense for our brand www.pawlowtide.ca

I need the final final to have contact info for:

Derek Osgood
Co-Owner
info@pawlowtide.ca
604-315-2780

and

Melissa Osgood
Co-Owner
info@pawlowtide.ca
604-347-5138

Target Market(s)

Female dog owners, 21 to 70

Industry/Entity Type

pet industry

Contact Information for Business Card

included in brief

Requirements
Should not have
• We do not want it to look cartonish

```html
<!DOCTYPE html>
<html lang="en">
<head>
<meta charset="utf-8">
<title>Pawlowtide Business Card</title>
<link rel="stylesheet" href="https://fonts.googleapis.com/css2?family=Montserrat:wght@400;500;600;700;800&family=Open+Sans:wght@400;600&display=swap">
<style>
  :root {
    --bg: #8e8e8e;
    --paper: #ffffff;
    --green: #9bd162;
    --green-dark: #7cc04a;
    --ink: #2b2b2b;
    --stripe: #333333;
    --ghost: #ececec;
  }
  * { margin: 0; padding: 0; box-sizing: border-box; }
  html, body { width: 1200px; height: 876px; overflow: hidden; }
  body {
    background: var(--bg);
    font-family: "Montserrat", sans-serif;
    color: var(--ink);
    position: relative;
  }
  .card {
    position: absolute;
    left: 320px;
    width: 560px;
    height: 320px;
    background: var(--paper);
    overflow: hidden;
    box-shadow: 0 6px 18px rgba(0,0,0,0.25);
  }
  .card--front { top: 88px; }
  .card--back { top: 468px; }

  .ghost-circle {
    position: absolute;
    border-radius: 50%;
    background: var(--ghost);
  }

  /* Front */
  .front-panel {
    position: absolute; left: 0; top: 0;
    width: 112px; height: 100%;
    background: var(--green);
  }
  .front-stripe {
    position: absolute; left: 112px; top: 0;
    width: 9px; height: 100%;
    background: var(--stripe);
  }
  .front-mark {
    position: absolute; left: 40px; top: 52px;
    width: 160px; height: 160px;
    border-radius: 50%;
    background: var(--green);
    border: 12px solid var(--paper);
  }
  .card--front .ghost-circle { width: 230px; height: 230px; left: 400px; top: 200px; }
  .front-brand {
    position: absolute; left: 214px; top: 150px;
    font-size: 50px; font-weight: 800; letter-spacing: -1px; line-height: 1;
  }
  .front-tagline {
    position: absolute; left: 218px; top: 208px;
    font-size: 13px; font-weight: 500; letter-spacing: 8px;
  }
  .person {
    position: absolute; left: 218px; top: 236px;
  }
  .person-name { font-size: 26px; font-weight: 600; line-height: 1.1; }
  .person-name .first { color: var(--green-dark); }
  .person-role { font-size: 10px; margin-top: 2px; }
  .person-contact {
    display: flex; align-items: center; gap: 8px;
    font-size: 11px; margin-top: 4px;
  }
  .person-contact .divider { width: 1px; height: 14px; background: var(--ink); }
  .person-contact svg { width: 13px; height: 13px; flex: none; }
  .contact-item { display: flex; align-items: center; gap: 4px; }

  /* Back */
  .card--back .ghost-circle { width: 230px; height: 230px; left: 350px; top: 90px; }
  .back-logo {
    position: absolute; left: 40px; top: 40px;
    display: flex; align-items: center; gap: 12px;
  }
  .back-logo .dot {
    width: 56px; height: 56px; border-radius: 50%; background: var(--green);
  }
  .back-brand { font-size: 42px; font-weight: 800; letter-spacing: -1px; line-height: 1; }
  .back-tagline {
    position: absolute; left: 112px; top: 94px;
    font-size: 11px; font-weight: 500; letter-spacing: 6px; color: var(--green-dark);
  }
  .back-band {
    position: absolute; left: 0; bottom: 0;
    width: 100%; height: 66px;
    background: var(--green);
    display: flex; align-items: center; padding-left: 60px;
  }
  .back-web {
    font-family: "Open Sans", sans-serif;
    font-size: 15px; font-weight: 600; letter-spacing: 6px; color: var(--ink);
  }
</style>
</head>
<body>

<section class="card card--front" aria-label="Card front">
  <div class="ghost-circle"></div>
  <div class="front-panel"></div>
  <div class="front-stripe"></div>
  <div class="front-mark"></div>
  <div class="front-brand">Pawlowtide</div>
  <div class="front-tagline">THE COAT REFRESHER</div>
  <div class="person">
    <div class="person-name"><span class="first">Derek</span> Osgood</div>
    <div class="person-role">Co-Owner</div>
    <div class="person-contact">
      <span class="contact-item">
        <svg viewBox="0 0 16 16"><circle cx="8" cy="8" r="7" fill="none" stroke="#7cc04a" stroke-width="1.4"/><path d="M5.5 4.5l1.5 1.5-1 1c.5 1.2 1.3 2 2.5 2.5l1-1 1.5 1.5-1 1c-2.5-.3-4.7-2.5-5-5z" fill="#7cc04a"/></svg>
        604-315-2780
      </span>
      <span class="divider"></span>
      <span class="contact-item">
        <svg viewBox="0 0 16 16"><rect x="1" y="3" width="14" height="10" fill="#7cc04a"/><path d="M1 3l7 6 7-6" fill="none" stroke="#fff" stroke-width="1.3"/></svg>
        info@pawlowtide.ca
      </span>
    </div>
  </div>
</section>

<section class="card card--back" aria-label="Card back">
  <div class="ghost-circle"></div>
  <div class="back-logo">
    <span class="dot"></span>
    <span class="back-brand">Pawlowtide</span>
  </div>
  <div class="back-tagline">THE COAT REFRESHER</div>
  <div class="back-band">
    <span class="back-web">www.pawlowtide.ca</span>
  </div>
</section>

</body>
</html>
```